Harborline Optical -Window Poster (Optometrist)

We are an optometry practice and we need a poster for a new store promotion for our window highlighting we now also sell 2 pairs of glasses as a package deal. The size will be 1300mm width x 1900mm height

The artwork will be displayed as a fabric banner in our shop window. We have 7 other banners with different services our business provides. The words needs to standout for passers by and the cars stopped at the traffic lights out front of our business. We already have signs with our logos phone number etc. so we won't need them included in the poster.

It would need to include the following information.

Two pair packages now available*

*Conditions apply
Updates

The artwork will be displayed as a fabric banner in our shop window. We have 7 other banners with different services our business provides. The words needs to standout for passers by and the cars stopped at the traffic lights out front of our business. We already have signs with our logos phone number etc. so we won't need them included in the poster. Thank you for your work it's amazing Added Saturday, February 18, 2017

The artwork will be displayed as a fabric banner in our shop window. We have 7 other banners with different services our business provides. The words needs to standout for passers by and the cars stopped at the traffic lights out front of our business. We already have signs with our logos phone number etc. so we won't need them included in the poster. Added Saturday, February 18, 2017

Target Market(s)

Cars driving past and stopped at traffic lights outside our store.

Industry/Entity Type

Optician

Requirements
Must have
• Poster must say:
• Two pair packages now available*
• *Conditions apply

```html
<!DOCTYPE html>
<html lang="en">
<head>
<meta charset="utf-8">
<title>Harborline Optical – Two Pair Packages Window Poster</title>
<link rel="stylesheet" href="https://fonts.googleapis.com/css2?family=Archivo+Black&family=Roboto+Condensed:wght@700&display=swap">
<style>
  :root {
    --night-top: #1b1f4a;
    --night-mid: #262b45;
    --board-dark: #1c1d26;
    --band: #0e0b20;
    --eyeball-light: #f2f2f4;
    --eyeball-shade: #a9abb2;
    --white: #ffffff;
    --yellow: #f5ec00;
  }
  html, body {
    margin: 0;
    padding: 0;
    width: 962px;
    height: 1200px;
    overflow: hidden;
    background: var(--board-dark);
  }
  .poster {
    position: relative;
    width: 962px;
    height: 1200px;
    overflow: hidden;
  }
  .backdrop {
    position: absolute;
    inset: 0;
    background: linear-gradient(180deg, var(--night-top) 0%, var(--night-mid) 30%, #2b2f40 45%, #23242f 70%, var(--board-dark) 100%);
  }
  .eyeball {
    position: absolute;
    left: 67px;
    top: 159px;
    width: 892px;
    height: 778px;
    border-radius: 50%;
    background: radial-gradient(circle at 45% 35%, var(--eyeball-light) 0%, #dcdde1 55%, var(--eyeball-shade) 100%);
  }
  .headline-top {
    position: absolute;
    left: 0;
    right: 0;
    top: 62px;
    text-align: center;
    font-family: "Roboto Condensed", sans-serif;
    font-weight: 700;
    font-size: 60px;
    letter-spacing: 2px;
    color: var(--white);
    margin: 0;
  }
  .headline-top sup {
    font-size: 62px;
    vertical-align: 0;
    position: relative;
    top: -12px;
    margin-left: 4px;
  }
  .band {
    position: absolute;
    left: 23px;
    width: 921px;
    background: var(--band);
    display: flex;
    align-items: center;
    font-family: "Archivo Black", sans-serif;
    line-height: 1;
    margin: 0;
  }
  .band--top {
    top: 228px;
    height: 194px;
    justify-content: center;
    font-size: 134px;
    color: var(--white);
  }
  .band--bottom {
    top: 599px;
    height: 195px;
    padding-left: 83px;
    box-sizing: border-box;
    font-size: 106px;
    color: var(--yellow);
  }
  .conditions {
    position: absolute;
    left: 121px;
    top: 1021px;
    width: 750px;
    height: 79px;
    box-sizing: border-box;
    border: 3px solid var(--white);
    display: flex;
    align-items: center;
    justify-content: center;
    font-family: "Roboto Condensed", sans-serif;
    font-weight: 700;
    font-size: 50px;
    letter-spacing: 2px;
    color: var(--white);
    margin: 0;
  }
</style>
</head>
<body>
  <main class="poster">
    <div class="backdrop" role="img" aria-label="Night sky over a dark wooden table with a pair of glasses resting on it"></div>
    <div class="eyeball" role="img" aria-label="Large glossy eyeball with a blue iris"></div>

    <p class="headline-top">NOW AVAILABLE<sup>*</sup></p>

    <h1 class="band band--top">TWO PAIR</h1>
    <h2 class="band band--bottom">PACKAGES</h2>

    <p class="conditions">*CONDITIONS APPLY</p>
  </main>
</body>
</html>
```